Mark & Lisa's Hammock Season Party

Invitation to a party 60-80 people at a private residence. Age range 30-40s.

Themes: summer/casual/Australian backyard/local community

**For delivery via both email and printed copy**
Would like one document suitable for both purposes or two versions for electronic or paper invitation. I will arrange printing so please prepare it in a suitable format.

Specimen text attached. Address and phone contact to follow by message with successful bidder

Thanks!
Mark

Target Market(s)

Locals, friends. Party attendees will typicaly be parents in their forties who who be leaving the kids at home for a relaxed party night, and walking home afterward

Industry/Entity Type

Community

Font styles to use
Sans Serif

Requirements
Should not have
• Cliche Australiana imagery. No kangaroos etc

```html
<!DOCTYPE html>
<html lang="en">
<head>
<meta charset="utf-8">
<title>Mark &amp; Lisa's Hammock Season Party</title>
<link rel="stylesheet" href="https://fonts.googleapis.com/css2?family=Playball&family=Oswald:wght@500&family=Abril+Fatface&family=Nunito+Sans:wght@800&family=Questrial&display=swap">
<style>
  :root {
    --paper: #f6f6f6;
    --red: #e0000f;
    --ink: #3b3b3b;
    --lights-top: #f3d6d8;
    --lights-bottom: #f6f6f6;
  }
  * { margin: 0; padding: 0; box-sizing: border-box; }
  html, body { width: 836px; height: 1200px; overflow: hidden; background: var(--paper); }
  .invitation { position: relative; width: 836px; height: 1200px; background: var(--paper); color: var(--ink); }

  .string-lights {
    position: absolute; left: 0; top: 0; width: 836px; height: 195px;
    background: linear-gradient(180deg, var(--lights-top) 0%, var(--lights-bottom) 100%);
  }

  .banner { position: absolute; left: 0; top: 212px; width: 836px; height: 90px; }
  .banner-text {
    position: absolute; top: 240px; height: 34px; line-height: 34px;
    font-family: "Oswald", sans-serif; font-weight: 500; font-size: 25px;
    color: #fff; text-transform: uppercase; letter-spacing: 0.2px; word-spacing: 2px;
  }
  .banner-text.left { left: 136px; }
  .banner-text.right { left: 446px; }
  .banner-amp {
    position: absolute; left: 404px; top: 230px; width: 32px; text-align: center;
    font-family: "Playball", cursive; font-size: 42px; line-height: 50px; color: #fff;
  }

  .title {
    position: absolute; left: 0; top: 318px; width: 836px; text-align: center;
    font-family: "Playball", cursive; font-weight: 400; font-size: 84px; line-height: 88px; color: var(--ink);
  }
  .red-line {
    position: absolute; left: 0; width: 836px; text-align: center;
    font-family: "Nunito Sans", sans-serif; font-weight: 800; color: var(--red);
    font-size: 37px; line-height: 42px;
  }
  .audience { top: 541px; }
  .day { top: 590px; }
  .time { top: 724px; }
  .address { top: 780px; font-size: 39px; line-height: 44px; }
  .rule { position: absolute; height: 3px; background: var(--red); }
  .date {
    position: absolute; left: 0; top: 626px; width: 836px; text-align: center;
    font-family: "Abril Fatface", serif; font-size: 98px; line-height: 100px; letter-spacing: 10px; color: var(--ink);
    padding-left: 10px;
  }
  .dotted { position: absolute; left: 86px; width: 668px; height: 8px; }

  .details {
    position: absolute; left: 0; top: 868px; width: 836px; list-style: none; text-align: center;
    font-family: "Questrial", sans-serif; font-size: 22px; line-height: 24px; color: var(--ink);
  }
  .details li { margin-bottom: 10px; }
  .details li::before {
    content: ""; display: inline-block; width: 15px; height: 15px; border-radius: 50%;
    background: var(--red); margin-right: 7px; vertical-align: -1px;
  }
</style>
</head>
<body>
<main class="invitation">
  <div class="string-lights" role="img" aria-label="Decorative string of red party lights hanging across the top"></div>

  <svg class="banner" viewBox="0 212 836 90" aria-hidden="true">
    <polygon fill="var(--red)" points="119,236 721,236 706,256 721,276 119,276 134,256"/>
    <polygon fill="var(--red)" points="420,211 427,224 440,215 441,230 456,228 449,241 463,246 451,255 463,265 449,270 456,283 441,281 440,296 427,287 420,300 413,287 400,296 399,281 384,283 391,270 377,265 389,255 377,246 391,241 384,228 399,230 400,215 413,224"/>
  </svg>
  <p class="banner-text left">Leave the kids at home</p>
  <p class="banner-amp">&amp;</p>
  <p class="banner-text right">Let your hair down at</p>

  <h1 class="title">Mark &amp; Lisa's<br>Hammock Season Party</h1>

  <p class="red-line audience">For Ferncliff Bay and friends</p>
  <span class="rule" style="left:83px; top:612px; width:236px;"></span>
  <p class="red-line day">Saturday</p>
  <span class="rule" style="left:516px; top:612px; width:237px;"></span>

  <p class="date">02.01.2016</p>

  <span class="rule" style="left:83px; top:744px; width:160px;"></span>
  <p class="red-line time">From 6pm 'til late</p>
  <span class="rule" style="left:592px; top:744px; width:161px;"></span>

  <p class="red-line address">25 Wattlebird Street, Ferncliff Bay</p>

  <svg class="dotted" style="top:838px;" viewBox="0 0 668 8" aria-hidden="true">
    <line x1="0" y1="4" x2="668" y2="4" stroke="var(--red)" stroke-width="7" stroke-dasharray="7 19.1"/>
  </svg>

  <ul class="details">
    <li>Child-free event</li>
    <li>Dress: summer casual, bare feet welcome</li>
    <li>Cocktail food provided</li>
    <li>BYO but only if you insist</li>
    <li>If you have some friends or neighbours that you like<br>to hang out with, we would love to meet. Bring them with you!</li>
    <li>An RSVP for catering would be nice.<br>Text Mark xxx xxxxxx or Lisa yyyyyyyy before Xmas please.</li>
  </ul>

  <svg class="dotted" style="top:1135px;" viewBox="0 0 668 8" aria-hidden="true">
    <line x1="0" y1="4" x2="668" y2="4" stroke="var(--red)" stroke-width="7" stroke-dasharray="7 19.1"/>
  </svg>
</main>
</body>
</html>
```